" Busco uma arte para capa de um livro que estou concluindo. Título do livro: "Entre marés e faróis. Um diário de viagens pelo litoral esquecido". "

```html
<!DOCTYPE html>
<html lang="pt-BR">
<head>
<meta charset="utf-8">
<title>Entre marés e faróis — capa</title>
<link rel="stylesheet" href="https://fonts.googleapis.com/css2?family=Oswald:wght@300;400;600&family=Crimson+Text:wght@400&display=swap">
<style>
  :root {
    --page-bg: #ebebeb;
    --cover-dark: #2b2b2b;
    --cover-mid: #3a3a3a;
    --cover-edge: #1f1f1f;
    --ink-light: #f2f2f2;
    --ink-soft: #d6d6d6;
    --frame-line: rgba(255,255,255,0.75);
    --art-light: #d9d9d9;
    --art-mid: #8f8f8f;
  }
  * { margin: 0; padding: 0; box-sizing: border-box; }
  html, body {
    width: 1200px; height: 1200px; overflow: hidden;
    background: var(--page-bg);
  }
  .canvas {
    position: relative; width: 1200px; height: 1200px;
    display: flex; align-items: center; justify-content: center;
  }
  .cover {
    position: relative; width: 740px; height: 1060px;
    background:
      radial-gradient(ellipse at 35% 30%, var(--cover-mid) 0%, var(--cover-dark) 60%, var(--cover-edge) 100%);
    box-shadow: 0 20px 50px rgba(0,0,0,0.25);
    overflow: hidden;
  }
  .cover-frame {
    position: absolute; inset: 26px;
    border: 1.5px solid var(--frame-line);
  }
  .author {
    position: absolute; left: 62px; top: 104px;
    font-family: "Crimson Text", Georgia, serif;
    font-size: 22px; letter-spacing: 1px;
    color: var(--ink-soft);
  }
  .title-block {
    position: absolute; left: 0; right: 0; top: 230px;
    text-align: center; color: var(--ink-light);
    font-family: "Oswald", "Arial Narrow", sans-serif;
    line-height: 0.95;
  }
  .title-lead {
    display: block; font-weight: 300; font-size: 64px;
    letter-spacing: 1px;
  }
  .title-main {
    display: block; font-weight: 600; font-size: 118px;
    letter-spacing: 1px;
  }
  .subtitle {
    display: block; margin-top: 14px;
    font-weight: 300; font-size: 32px; line-height: 1.15;
    color: var(--ink-soft); letter-spacing: 0.5px;
  }
  .cover-art {
    position: absolute; left: 130px; top: 560px;
    width: 500px; height: 340px;
  }
</style>
</head>
<body>
  <main class="canvas">
    <article class="cover">
      <div class="cover-frame"></div>
      <p class="author">Otávio Lemos de Andrade</p>
      <h1 class="title-block">
        <span class="title-lead">entre marés</span>
        <span class="title-main">e faróis</span>
        <span class="subtitle">um diário de viagens<br>pelo litoral esquecido</span>
      </h1>
      <svg class="cover-art" viewBox="0 0 500 340" role="img" aria-label="Gravura em preto e branco de uma mão com punho de camisa segurando uma pena de escrever">
        <defs>
          <radialGradient id="artGlow" cx="55%" cy="45%" r="60%">
            <stop offset="0%" stop-color="var(--art-light)" stop-opacity="0.85"/>
            <stop offset="70%" stop-color="var(--art-mid)" stop-opacity="0.35"/>
            <stop offset="100%" stop-color="var(--art-mid)" stop-opacity="0"/>
          </radialGradient>
        </defs>
        <rect width="500" height="340" fill="url(#artGlow)"/>
      </svg>
    </article>
  </main>
</body>
</html>
```